Business Card Design Brookvale Flooring

We are a Mobile Flooring Company servicing the Central Coast NSW and Newcastle.We sell and Install Bamboo flooring, laminate flooring and engineered flooring to do it yourself renovators, builders and home improvement clientsOur prices are very competitive and we have a great colour range and selection.We would like the front of the card to have the wood floorboard image (perhaps as the background) and then have our logo over the top (large) with the logo in spot gloss and all the writing in spot gloss. Details of what we do can be included on the back with the deer image (perhaps in silhouette) in the background. Any other ideas using these images will be appreciated.

Target Market(s)

DIY renovators, builders, home improvement clients

Industry/Entity Type

Flooring

Contact Information for Business Card

Servicing Central Coast to Newcastle
sales@brookvaleflooring.com.au
0438 216 504
www.brookvaleflooring.com.au

Font styles to use
Other font styles liked:
• You decide

Requirements
Must have
• The project must have both files uploaded on the business card the image of the woodland forest/ floorboards in the background - filling the whole business card or half business card with the logo over the top
• The logo and all the writing needs to be spot gloss
Nice to have
• A clear easy to read attractive business card
Should not have
• Too dark

```html
<!DOCTYPE html>
<html lang="en">
<head>
<meta charset="utf-8">
<title>Brookvale Flooring – Business Card</title>
<link rel="stylesheet" href="https://fonts.googleapis.com/css2?family=Open+Sans:wght@400;600;700&display=swap">
<style>
  :root {
    --page-bg: #e9e7e4;
    --ink: #2b2b2d;
    --white: #ffffff;
    --forest-light: #8fbf4a;
    --forest-mist: #e8f0dc;
    --forest-dark: #1c2a1c;
    --forest-deep: #0f1a12;
    --forest-glow: #3a7a3a;
    --wood-pale: #c4844a;
    --wood-light: #b57338;
    --wood-mid: #9a5a28;
    --wood-dark: #6e3c18;
    --mark-green: #2f8f46;
  }
  * { margin: 0; padding: 0; box-sizing: border-box; }
  html, body {
    width: 1200px; height: 1000px; overflow: hidden;
    background: var(--page-bg);
    font-family: "Open Sans", Arial, sans-serif;
  }
  .canvas { position: relative; width: 1200px; height: 1000px; }
  .card {
    position: absolute; left: 265px; width: 665px; height: 396px;
    overflow: hidden; box-shadow: 0 4px 14px rgba(0,0,0,0.25);
  }
  .card--front { top: 72px; background: var(--white); }
  .card--back { top: 532px; background: var(--forest-deep); }

  .forest-photo { position: absolute; left: 0; top: 0; width: 665px; height: 283px; }
  .card--front .forest-photo {
    background: linear-gradient(180deg, var(--forest-light) 0%, #b9d58a 35%, var(--forest-mist) 65%, var(--white) 82%);
  }
  .card--back .forest-photo {
    background: radial-gradient(ellipse 120px 150px at 330px 130px, var(--forest-glow) 0%, rgba(58,122,58,0) 100%),
                linear-gradient(180deg, var(--forest-dark) 0%, #223622 60%, #1a2e1c 100%);
  }
  .floor-photo {
    position: absolute; left: 0; top: 283px; width: 665px; height: 113px;
    background: linear-gradient(90deg, var(--wood-mid) 0%, var(--wood-pale) 20%, var(--wood-light) 50%, var(--wood-pale) 75%, var(--wood-dark) 100%);
  }
  .card--back .floor-photo {
    background: linear-gradient(90deg, var(--wood-dark) 0%, var(--wood-mid) 25%, var(--wood-light) 50%, var(--wood-mid) 75%, var(--wood-dark) 100%);
  }

  .brand {
    position: absolute; left: 100px; top: 172px;
    display: inline-flex; flex-direction: column; align-items: flex-end;
    color: var(--ink); line-height: 1;
  }
  .brand__name { font-size: 66px; font-weight: 600; letter-spacing: -1.5px; }
  .brand__sub { font-size: 22px; font-weight: 400; letter-spacing: 0.5px; margin-top: 2px; }
  .brand-mark {
    position: absolute; left: 432px; top: 108px;
    width: 150px; height: 150px; border-radius: 50%;
    background: var(--ink);
  }

  .service-area {
    position: absolute; left: 302px; top: 288px;
    font-size: 15px; font-weight: 700; color: var(--ink);
  }
  .contact { position: absolute; left: 38px; top: 303px; list-style: none; }
  .contact li {
    display: flex; align-items: center; gap: 7px;
    height: 18px; font-size: 14px; font-weight: 700; color: var(--ink);
  }
  .contact svg { width: 12px; height: 12px; fill: var(--ink); flex: none; }

  .watermark {
    position: absolute; left: 38px; top: 224px;
    font-size: 34px; font-weight: 600; color: var(--mark-green); opacity: 0.75;
  }
  .about {
    position: absolute; left: 0; top: 290px; width: 665px; text-align: center;
    color: var(--white); font-size: 14px; font-weight: 600; line-height: 21px;
  }
  .about p + p { margin-top: 6px; }
</style>
</head>
<body>
<main class="canvas">
  <section class="card card--front">
    <div class="forest-photo" role="img" aria-label="Sunlit forest of tall trees fading into white"></div>
    <div class="floor-photo" role="img" aria-label="Timber floorboards in perspective"></div>
    <div class="brand-mark"></div>
    <div class="brand">
      <span class="brand__name">Brookvale</span>
      <span class="brand__sub">FLOORING</span>
    </div>
    <div class="service-area">Servicing Central Coast to Newcastle</div>
    <ul class="contact">
      <li><svg viewBox="0 0 24 24"><path d="M6.6 10.8a15 15 0 0 0 6.6 6.6l2.2-2.2c.3-.3.7-.4 1-.2 1.1.4 2.3.6 3.6.6.6 0 1 .4 1 1V20c0 .6-.4 1-1 1A17 17 0 0 1 3 4c0-.6.4-1 1-1h3.5c.6 0 1 .4 1 1 0 1.3.2 2.5.6 3.6.1.3 0 .7-.2 1z"/></svg>0438 216 504</li>
      <li><svg viewBox="0 0 24 24"><path d="M2 5h20v14H2V5zm2 2v.3l8 6 8-6V7H4z"/></svg>sales@brookvaleflooring.com.au</li>
      <li><svg viewBox="0 0 24 24"><path d="M12 2a10 10 0 1 0 0 20 10 10 0 0 0 0-20zm6.9 6h-3a15 15 0 0 0-1.3-4 8 8 0 0 1 4.3 4zM12 4c.8 1.2 1.5 2.5 1.9 4h-3.8c.4-1.5 1.1-2.8 1.9-4zM4.3 14a8 8 0 0 1 0-4h3.4a16 16 0 0 0 0 4H4.3zm.8 2h3a15 15 0 0 0 1.3 4 8 8 0 0 1-4.3-4zm3-8h-3a8 8 0 0 1 4.3-4 15 15 0 0 0-1.3 4zM12 20c-.8-1.2-1.5-2.5-1.9-4h3.8c-.4 1.5-1.1 2.8-1.9 4zm2.3-6H9.7a14 14 0 0 1 0-4h4.6a14 14 0 0 1 0 4zm.3 6a15 15 0 0 0 1.3-4h3a8 8 0 0 1-4.3 4zm1.7-6a16 16 0 0 0 0-4h3.4a8 8 0 0 1 0 4h-3.4z"/></svg>www.brookvaleflooring.com.au</li>
    </ul>
  </section>

  <section class="card card--back">
    <div class="forest-photo" role="img" aria-label="Dark forest with a glowing green stag silhouette among the trees"></div>
    <div class="floor-photo" role="img" aria-label="Timber floorboards in perspective"></div>
    <div class="watermark">Brookvale</div>
    <div class="about">
      <p>We supply floating flooring for builders and DIY renovators including<br>bamboo, laminates and engineered timber flooring in a range of colours.</p>
      <p>We also offer an installation service.</p>
    </div>
  </section>
</main>
</body>
</html>
```